E-Liquid Label Design for Lantern Mist

We need a new design for the labels we use on our product, which are bottles of e-liquid for use in e-cigarettes. We have attached our original label (which we are using now) so you can see what we are using. We would like a new design that is classier, like the label on a high end bottle of rum or whisky, but with a little bit of a modern flair. I have also attached examples of our competitors bottles. We do not necessarily want our new design to be too similar to these, in an effort to avoid copying them, but we want the new design to be up to par with them in terms of quality and appeal.
The label must contain the following information:
- Bottle Size : 30ml
- Type of blend (Either 50PG/50VG or 70PG/30VG). The new design can have this set statically. We only included both options on the original label because we manually mark this with a marker depending on what blend it is. We no longer want to do this. We just want the one blend, whatever it is to be on the label.
- The line "Orchard Drip" (as this is the name of the line)
- The line "Premium E-Liquid" in smaller caps right under "Orchard Drip"
- The Flavor Name
- The Nicotine strength. You can use the example strength "FULL | 2.4 Nicotine"
- The Ingredients and Warning. See original label for text (Including "Shake Well")
- A small white box where a UPC barcode can be placed
Use the color theme on the original label, but you can mix it up and use more of one color than another. Be as creative as possible. Classy & Tropical would be what someone would think of when looking at this new design.
Our High Res Logo is also attached.New Label stock that will be used with be white high gloss 1X2.5
The final design must be in .svg format so we can change the variables, like bottles size, flavor, etc when printing.

```html
<!DOCTYPE html>
<html lang="en">
<head>
<meta charset="utf-8">
<title>Lantern Mist – Orchard Drip Label</title>
<link href="https://fonts.googleapis.com/css2?family=Oswald:wght@500;700&family=Archivo+Narrow:wght@400;700&family=Archivo+Black&family=PT+Serif&family=Roboto+Condensed:wght@400;700&display=swap" rel="stylesheet">
<style>
  :root {
    --leaf-deep: #1d6b22;
    --leaf-mid: #2f9a35;
    --leaf-bright: #5cc24a;
    --lime: #b9e04f;
    --ink-green: #1c4f1e;
    --ink: #111;
    --paper: #fff;
    --frame: #cfcfcf;
  }
  * { box-sizing: border-box; margin: 0; padding: 0; }
  html, body { width: 1200px; height: 506px; overflow: hidden; background: #fff; }
  .label {
    position: relative; width: 1200px; height: 506px; overflow: hidden;
    border: 3px solid var(--frame); border-radius: 10px;
  }
  .backdrop {
    position: absolute; inset: 0;
    background: radial-gradient(ellipse at 55% 45%, var(--lime) 0%, var(--leaf-bright) 22%, var(--leaf-mid) 50%, var(--leaf-deep) 100%);
  }
  .swoosh { position: absolute; inset: 0; }
  .vertical {
    position: absolute; writing-mode: vertical-rl; transform: rotate(180deg);
    white-space: nowrap;
  }
  .size {
    left: 196px; top: 40px; height: 150px;
    font: 700 62px/1 "Oswald", sans-serif; color: var(--ink-green);
    text-align: center;
  }
  .blend {
    left: 262px; top: 34px; height: 170px;
    font: 700 25px/1 "Oswald", sans-serif; color: var(--ink-green);
    text-align: center;
  }
  .upc-box {
    position: absolute; left: 38px; top: 250px; width: 280px; height: 222px;
    background: var(--paper); border: 1px solid #ddd;
  }
  .brand {
    left: 352px; top: 30px; height: 446px;
    font: 700 72px/1 "Oswald", sans-serif; color: var(--leaf-deep);
    text-align: center; letter-spacing: 2px;
  }
  .product {
    position: absolute; left: 576px; top: 26px; width: 300px;
  }
  .product-line { font: 400 42px/1 "Archivo Black", sans-serif; color: var(--ink); letter-spacing: 0.5px; }
  .product-sub { font: 400 22px/1 "PT Serif", serif; color: var(--ink); letter-spacing: 1.5px; margin-top: 10px; }
  .strength { font: 400 26px/1 "Archivo Narrow", sans-serif; color: var(--ink); margin-top: 14px; }
  .strength b { font-weight: 700; }
  .flavor {
    position: absolute; left: 620px; top: 356px; width: 250px;
    font: 700 31px/1.45 "Archivo Narrow", sans-serif; color: var(--ink); text-align: center;
  }
  .notice {
    left: 900px; top: 14px; height: 478px;
    font: 400 24.5px/1.16 "Roboto Condensed", sans-serif; color: var(--paper);
  }
  .notice b { font-weight: 700; }
</style>
</head>
<body>
<div class="label">
  <div class="backdrop" role="img" aria-label="Sweeping tropical green leaf streaks background"></div>
  <svg class="swoosh" width="1200" height="506" viewBox="0 0 1200 506" aria-hidden="true">
    <path d="M336 0 H1000 C930 120 760 180 560 232 C720 290 860 380 890 506 H336 Z" fill="var(--paper)"/>
    <path d="M560 232 C720 290 860 380 890 506 H860 C820 400 700 310 560 232 Z" fill="var(--leaf-bright)" opacity="0.35"/>
  </svg>

  <div class="vertical size">30ml</div>
  <div class="vertical blend">50PG/50VG</div>
  <div class="upc-box"></div>

  <div class="vertical brand">LANTERN MIST</div>

  <div class="product">
    <div class="product-line">ORCHARD DRIP</div>
    <div class="product-sub">PREMIUM E-LIQUID</div>
    <div class="strength"><b>FULL</b> | 2.4 Nicotine</div>
  </div>

  <div class="flavor">CHOCOLATE<br>PEANUT<br>BUTTER CUP</div>

  <div class="vertical notice">
    <b>Ingredients:</b> USP Grade<br>
    Vegetable Glycerin,<br>
    USP Grade Propylene Glycol,<br>
    Natural Flavors, Artificial Flavors.<br>
    <b>WARNING:</b> Keep out of reach<br>
    of children. Must be 18 or older.<br>
    <b>Do not drink. Shake well.</b>
  </div>
</div>
</body>
</html>
```